I need a business card design for a new company that will be doing consulting work around issues of cultural competency, and diversity and inclusion. I would like the design to be crisp and clear with bold but conservative colors and incorporate shades of blue

Target Market(s)

Small businesses, schools, non-profits

Industry/Entity Type

Consulting

Font styles to use
Serif
Sans Serif

Colors
0c5ba6
6b449b
3276b5
0292cd

Requirements
Must have
• A Morrow Venture (name of company)
• Lemlem Tavish
• CEO
• lemlem@amorrowventure.com
• (215)483-2756

```html
<!DOCTYPE html>
<html lang="en">
<head>
<meta charset="utf-8">
<title>Lemlem Tavish — Business Card</title>
<link rel="stylesheet" href="https://fonts.googleapis.com/css2?family=League+Spartan:wght@700&family=Jost:wght@300;500&display=swap">
<style>
  :root {
    --card-white: #ffffff;
    --panel-grey: #e8e8ea;
    --accent-purple: #6b449b;
    --name-black: #0a0a0a;
    --name-blue: #3276b5;
    --company-blue: #0c5ba6;
    --title-grey: #555555;
  }
  html, body {
    margin: 0;
    padding: 0;
    overflow: hidden;
    background: var(--card-white);
  }
  .card {
    position: relative;
    width: 1200px;
    height: 686px;
    background: var(--card-white);
    overflow: hidden;
  }
  .card__shapes {
    position: absolute;
    inset: 0;
    width: 1200px;
    height: 686px;
  }
  .shape--panel { fill: var(--panel-grey); }
  .shape--wedge { fill: var(--accent-purple); }

  .identity {
    position: absolute;
    left: 623px;
    top: 300px;
    transform: translateX(-50%);
    text-align: right;
  }
  .identity__name {
    margin: 0;
    font-family: "League Spartan", "Futura", sans-serif;
    font-weight: 700;
    font-size: 98px;
    line-height: 1;
    letter-spacing: -1px;
    white-space: nowrap;
  }
  .identity__first { color: var(--name-black); }
  .identity__last { color: var(--name-blue); }
  .identity__role {
    margin: 4px 14px 0 0;
    font-family: "Jost", sans-serif;
    font-weight: 300;
    font-size: 30px;
    line-height: 1;
    color: var(--title-grey);
    letter-spacing: 0.5px;
  }

  .contact {
    position: absolute;
    right: 90px;
    bottom: 56px;
    text-align: right;
    font-family: "Jost", sans-serif;
    line-height: 1.35;
  }
  .contact__company {
    margin: 0 0 8px;
    font-weight: 500;
    font-size: 26px;
    letter-spacing: 1px;
    color: var(--company-blue);
  }
  .contact__line {
    margin: 0;
    font-weight: 300;
    font-size: 21px;
    color: var(--title-grey);
  }
</style>
</head>
<body>
  <div class="card">
    <svg class="card__shapes" viewBox="0 0 1200 686" aria-hidden="true">
      <polygon class="shape--panel" points="0,0 528,0 598,221 135,560 0,560"/>
      <polygon class="shape--wedge" points="0,154 171,686 0,686"/>
    </svg>
    <div class="identity">
      <h1 class="identity__name"><span class="identity__first">Lemlem</span> <span class="identity__last">Tavish</span></h1>
      <p class="identity__role">CEO</p>
    </div>
    <div class="contact">
      <p class="contact__company">A Morrow Venture</p>
      <p class="contact__line">lemlem@amorrowventure.com</p>
      <p class="contact__line">(215)483-2756</p>
    </div>
  </div>
</body>
</html>
```